Colourful Bold Design for Pet Insurance Website

PLEASE NOTE THAT THIS PROJECT HAS BEEN EXTENDED. Please read the PROJECT EXTENSION DOCUMENT BEFORE STARTING WORK ON ANY DESIGNS.

We are looking for a colourful bold new template design for our JOOMLA HOMEPAGE and a matching design for our new WORDPRESS BLOG.

The website will help pet owners work out which insurance policy best meets their needs. The aim of the website is to explain policy differences in a plain clear manner.

The website will need to have a professional colourful image. It needs to be BOLD, CLEAN AND SHARP rather than soft, pastel and cuddly.

COLOUR SCHEME
The website needs to have a bold colourful design on a white background.
On the inner pages we will have five different types of policies which will be colour coded. We would ideally therefore like to incorporate five distinct colours in the design. See attached document for example of colour schemes we like.

LOGO
We want to keep the existing logo. Please find the file attached. You may though change the logo colours.

CONTENT
One of the reasons for the new design is that we want to change the style of the homepage and include new content. Our current homepage can be found at www.furrow-cover-polls.co.uk.

Content Required
Slideshow
Article Intro.. About Pet Insurance
Policy Lookup Box (see existing site… you can change the design of this)
Six link options (see links on left of current page)
Latest Reviews (List of 6)
Ad (Same dimensions as currently on homepage)

News and Comment Section - To include Three or Four Articles, Title, Intro to article (probably 3 or 4 lines .. about 400px wide), Read more link
Social Media Section
Facebook Plugin with Feed
Latest Tweets Plugin
Pet Charities Latest Tweets
Footer
Larger footer with lots of links grouped in sections

It does not need to include the clipart pic of the pets which is on the current homepage.

Examples of Websites and Templates We Like
http://www.pawlane.com/ (like colours… fonts…layout)
http://sitetheme.brightkiln.com/?template=upbeat&path=/... (like the clarity, "white" space etc)
http://www.layoutforge.com/demo/51872.html (like white space, clear easy to read fonts… don’t like colour scheme, size of top picture)
http://www.layoutforge.com/website-templates/63915.html (like colour scheme, use of white space)

FEEDBACK
I will provide lots of feedback on all designs submitted so that together we can get the best result.

For clarification this is a DESIGN ONLY project. Our website developer will view the designs before we make our final choice as he wants to ensure he can develop "sharp, practical and most importantly light weight web interface" from the design.

Just updated this brief to clarify design issues, content issues and to give some more examples of site designs I like. 

Please note that although we wish to keep the logo you can change the colours to suit your design. 

Please note that we have now added details of pictures we would be happy to use on the website.  We would prefer it if you used one of these.   Otherwise please ensure your picture includes a nice dog and nice cat and no people!

I have been delighted with the quality of the designs submitted for this project.  So much so that I am going to extend the project to include some additional inner pages.   The amended brief will be posted on here on Friday 10 May.   The deadline will be extended and the budget will also be increased. 

Reason: Additional inner pages now required. Budget will be increased. Revised brief to be posted on here Friday 10 May.

Target Market(s)

Pet owners in the UK who are confused about pet insurance. It therefore needs to be a bold design which is plain, clean and easy to read. It should use bold colours rather than pastels and should not use "cuddly" images.

Industry/Entity Type

Insurance

Requirements
Must have
• Bold clear and distinct colours (preferably 5)
Content as per uploaded file (not just content from existing site)
Easy to read fonts
Should not have
• Pastel colours
Cuddly images

```html
<!DOCTYPE html>
<html lang="en">
<head>
<meta charset="utf-8">
<title>Furrow Cover Polls UK — Home</title>
<link rel="stylesheet" href="https://fonts.googleapis.com/css2?family=Libre+Baskerville:wght@400;700&display=swap">
<style>
  :root {
    --blue: #0e9ad9;
    --blue-dark: #0a7fc0;
    --blue-deep: #1f6fb0;
    --green: #22a01a;
    --orange: #f4511a;
    --purple: #9a4fd0;
    --panel: #f5f5f4;
    --rule: #dcdcdc;
    --text: #555;
    --white: #fff;
  }
  * { box-sizing: border-box; margin: 0; padding: 0; }
  html, body { width: 1200px; height: 1023px; overflow: hidden; background: var(--white); }
  body { position: relative; font-family: "Libre Baskerville", Georgia, serif; color: var(--text); }
  .abs { position: absolute; }

  .page-column { left: 317px; top: 0; width: 528px; height: 860px; border-left: 2px solid #e4e4e4; border-right: 2px solid #e4e4e4; }
  .top-accent { left: 319px; top: 0; width: 138px; height: 3px; background: var(--purple); }

  .report-band { left: 319px; top: 39px; width: 352px; height: 81px; background: var(--panel); }
  .report-arrow { left: 319px; top: 39px; width: 185px; height: 81px; }
  .report-title { left: 327px; top: 50px; width: 160px; font-size: 21px; line-height: 28px; color: var(--white); font-weight: 700; }
  .report-due { left: 519px; top: 74px; font-size: 9px; font-weight: 700; color: #333; }

  .section-bar { height: 30px; background: repeating-linear-gradient(135deg, var(--blue) 0 4px, #1aa3e0 4px 8px); color: var(--white); font-weight: 700; font-size: 14px; padding: 6px 10px; border-bottom: 3px solid var(--blue-dark); }
  .news-bar { left: 328px; top: 150px; width: 343px; }
  .comment-bar { left: 328px; top: 379px; width: 334px; clip-path: polygon(0 0, 100% 0, 93% 50%, 100% 100%, 0 100%); padding-left: 14px; }

  .news-title { left: 341px; top: 204px; font-size: 15px; color: var(--blue); }
  .news-intro { left: 351px; top: 230px; width: 165px; font-size: 10.5px; line-height: 18px; color: #666; word-break: break-all; }
  .news-photo { left: 529px; top: 201px; width: 137px; height: 102px; background: radial-gradient(circle at 55% 50%, #c98a3c 0 32%, #e8d3b4 55%, #f3efe9 80%); }
  .btn-more { background: var(--orange); color: var(--white); font-size: 8.5px; font-weight: 700; padding: 4px 4px; }
  .news-more { left: 610px; top: 315px; }
  .news-rule { left: 328px; top: 353px; width: 343px; height: 3px; background: var(--blue-deep); }

  .comment-card { top: 408px; width: 162px; height: 136px; background: var(--panel); }
  .comment-card-head { position: absolute; left: 8px; top: 15px; width: 147px; height: 28px; background: var(--blue); color: var(--white); font-size: 14px; padding: 5px 7px; }
  .comment-card-text { position: absolute; left: 17px; top: 52px; width: 128px; font-size: 5.5px; line-height: 9px; color: #888; word-break: break-all; }
  .comment-card .btn-more { position: absolute; left: 80px; top: 97px; }

  .review-card { width: 113px; height: 97px; border: 1px solid #5aa9d4; background: var(--panel); }
  .review-card-head { height: 30px; background: repeating-linear-gradient(135deg, var(--blue) 0 4px, #1aa3e0 4px 8px); border-bottom: 2px solid var(--blue-dark); color: var(--white); font-size: 10px; font-weight: 700; padding: 9px 8px; }

  .side-box { left: 685px; width: 151px; background: var(--blue); border-radius: 4px; padding: 8px 8px; color: var(--white); font-size: 8px; font-weight: 700; }
  .side-box span { display: block; border-bottom: 1px solid #8fd0ef; padding-bottom: 3px; }

  .help-head { left: 683px; top: 230px; width: 153px; height: 39px; background: #ececec; color: var(--blue); font-size: 12.5px; padding: 12px 7px; }
  .help-lead { left: 690px; top: 279px; width: 135px; font-size: 8px; line-height: 14px; }
  .help-flag { left: 688px; width: 93px; height: 21px; background: var(--blue); clip-path: polygon(0 0, 100% 50%, 0 100%); color: var(--white); font-size: 8.5px; font-weight: 700; padding: 4px 4px; }
  .help-text { left: 693px; width: 135px; font-size: 5.5px; line-height: 10px; }
  .help-text b { color: var(--blue); }

  .notice { left: 684px; top: 577px; width: 152px; height: 150px; background: repeating-linear-gradient(135deg, var(--orange) 0 5px, #f75c27 5px 10px); color: var(--white); font-size: 6.5px; font-weight: 700; line-height: 10.5px; padding: 9px 9px; }

  .footer-strip { left: 288px; top: 859px; width: 585px; height: 6px; background: #ddd; }
  .footer { left: 288px; top: 865px; width: 585px; height: 158px; background: repeating-linear-gradient(135deg, var(--blue) 0 5px, #15a0dd 5px 10px); }
  .brand { left: 319px; top: 887px; display: flex; align-items: center; gap: 7px; }
  .brand-dot { width: 32px; height: 32px; border-radius: 50%; background: var(--white); }
  .brand-name { width: 125px; font-size: 13px; line-height: 15px; font-weight: 700; color: var(--white); }
  .social-box { left: 319px; top: 942px; width: 169px; height: 64px; background: var(--blue-dark); padding: 9px 8px; }
  .social-row { display: flex; gap: 13px; margin-left: 7px; }
  .social-row i { width: 20px; height: 20px; border-radius: 50%; background: var(--white); }
  .search { margin-top: 9px; display: flex; align-items: center; gap: 4px; color: var(--white); font-size: 9px; font-weight: 700; }
  .search i { width: 119px; height: 15px; background: var(--white); border-radius: 2px; }
  .footer-links { top: 892px; list-style: none; font-size: 7.5px; line-height: 13px; font-weight: 700; color: var(--white); }
  .copyright { left: 525px; top: 1011px; font-size: 6px; font-weight: 700; color: var(--white); }
</style>
</head>
<body>
  <div class="abs page-column"></div>
  <div class="abs top-accent"></div>

  <div class="abs report-band"></div>
  <svg class="abs report-arrow" viewBox="0 0 185 81"><polygon points="0,0 137,0 185,40.5 137,81 0,81" fill="var(--green)"/></svg>
  <div class="abs report-title">2013 Price Survey Report</div>
  <div class="abs report-due">Due April 2013.</div>

  <div class="abs section-bar news-bar">Latest News</div>
  <h2 class="abs news-title" style="font-weight:400">Title</h2>
  <p class="abs news-intro">Intro to article xxxxxxxxxxx xxxxxxxxxxxxxxxxxxxxxxxx xxxxxxxxxxxxxxxxxxxxxxxx xxxxxxxxxxxxxxxxxxxxxxx</p>
  <div class="abs news-photo" role="img" aria-label="Photo of a golden retriever on a white background"></div>
  <a class="abs btn-more news-more">Read More</a>
  <div class="abs news-rule"></div>

  <div class="abs section-bar comment-bar">Comment</div>
  <article class="abs comment-card" style="left:328px">
    <div class="comment-card-head">Title</div>
    <p class="comment-card-text">Intro to article xxxxxxxxxxxx xxxxxxxxxxxxxxxxxxxxxxxxxxx xxxxxxxxxxxxxxxxxxxxxxxxx xxxxxxxxxxxxxxxxxxxxxxxx</p>
    <a class="btn-more">Read More</a>
  </article>
  <article class="abs comment-card" style="left:495px">
    <div class="comment-card-head" style="top:13px">Title</div>
    <p class="comment-card-text">Intro to article xxxxxxxxxxxx xxxxxxxxxxxxxxxxxxxxxxxxxxx xxxxxxxxxxxxxxxxxxxxxxxxx xxxxxxxxxxxxxxxxxxxxxxxx</p>
    <a class="btn-more">Read More</a>
  </article>

  <div class="abs review-card" style="left:319px;top:576px"><div class="review-card-head">Latest Reviews</div></div>
  <div class="abs review-card" style="left:440px;top:576px"><div class="review-card-head">Latest Reviews</div></div>
  <div class="abs review-card" style="left:558px;top:576px"><div class="review-card-head">Latest Reviews</div></div>
  <div class="abs review-card" style="left:319px;top:681px"><div class="review-card-head">Latest Reviews</div></div>
  <div class="abs review-card" style="left:440px;top:681px"><div class="review-card-head">Latest Reviews</div></div>
  <div class="abs review-card" style="left:558px;top:681px"><div class="review-card-head">Latest Reviews</div></div>

  <div class="abs side-box" style="top:5px;height:78px"><span>Latest Tweets Plugin</span></div>
  <div class="abs side-box" style="top:105px;height:106px"><span>Pet Charities Latest Tweets</span></div>

  <div class="abs help-head">How can FCPP help you</div>
  <p class="abs help-lead">When choosing a pet insurance policy you will need to consider</p>
  <div class="abs help-flag" style="top:315px">Premium</div>
  <p class="abs help-text" style="top:344px">FCPP will publish regular <b>premium surveys</b> to help you identify policies which may give you a competitive quote.</p>
  <div class="abs help-flag" style="top:388px">Experience</div>
  <p class="abs help-text" style="top:419px">With your help FCPP will publish<br><b>claims experience ratings and surveys</b></p>
  <div class="abs help-flag" style="top:458px">Terms</div>
  <p class="abs help-text" style="top:490px">FCPP provides three pages of <b>detailed information</b> about each policy. For most popular policies we have also studied the terms in detail and identified those which we think you would want to know about.</p>

  <div class="abs notice">
    <p>Please read<br>We are passionate about making FCPP an invaluable resource for pet owners and therefore we have taken great care to ensure the information is as accurate and up-to-date as possible.</p>
    <p style="margin-top:10px">So please if you find any information you believe to be inaccurate then use the orange "Problem?" tab to let us know! We will check it out as soon as possible and correct the information if necessary.</p>
  </div>

  <div class="abs footer-strip"></div>
  <footer class="abs footer"></footer>
  <div class="abs brand"><i class="brand-dot"></i><span class="brand-name">Furrow Cover Polls UK</span></div>
  <div class="abs social-box">
    <div class="social-row"><i></i><i></i><i></i><i></i><i></i></div>
    <div class="search">Search <i></i></div>
  </div>
  <ul class="abs footer-links" style="left:523px">
    <li>» Home</li><li>Policies</li><li>Glossary</li><li>Fact Sheets</li><li>Survey Reports</li><li>News &amp; Comment</li>
  </ul>
  <ul class="abs footer-links" style="left:631px">
    <li>» Policy Files</li><li>Policy Search</li><li>Fact Sheets</li><li>Policy listings by type</li><li>Claims surveys</li><li>2013 Price Survey Report</li><li>Privacy Policy</li>
  </ul>
  <ul class="abs footer-links" style="left:753px;top:890px">
    <li>» Legal</li><li>About Furrow Cover</li><li>Polls UK</li><li>Problems</li><li>Cookies</li>
  </ul>
  <p class="abs copyright">Copyright © Furrow Cover Policy Polls</p>
</body>
</html>
```